Job Coaching - Vanta; engaging people to improve their work experience

I need a flyer for Job Coaching. It serves to engage customers (not businesses) with problems in their daily job, typical questions that are handled are:
Do I fit for the job?
Am I using my talents at best in this job?
I have a conflict with my manager/colleagues, what should I do?
My work-life balance is a mess, how can I improve this?
What job fits best with my talents?
I'm getting stressed out from my job, what can I do?
....
This Flyer will be available at GP's, therpeutic practices, pharamcists,...
this flyer should put people in action to contact me
Flyer can be created in English, in the final one the text should be in Dutch; I will make the translation of the selected flyer and provide it at the end

Target Market(s)

consumers / customers / people having a job, but somewhat stuck in it

Industry/Entity Type

Professional Coaching

Requirements
Must have
• the questions mentioned in the project description; mobile number: 0471/389145; email: tom.vermeer@vantacoaching.example; website: www.vantacoaching.example ; it should make also reference to 'Career guidance cheques of the KWOL'

```html
<!DOCTYPE html>
<html lang="en">
<head>
<meta charset="utf-8">
<title>Vanta Professional Job Coaching Flyer</title>
<link rel="stylesheet" href="https://fonts.googleapis.com/css2?family=Montserrat:wght@400;500;600;700;800;900&display=swap">
<style>
:root{
  --teal:#35a99d;
  --teal-dark:#2a8d83;
  --ink:#111111;
  --grey-text:#555555;
  --paper:#ffffff;
  --paper-grey:#ebebeb;
  --navy:#1c3f7a;
  --backdrop:#3b3b3d;
}
*{box-sizing:border-box;margin:0;padding:0}
html,body{width:1200px;height:776px;overflow:hidden}
body{background:var(--backdrop);font-family:"Montserrat",sans-serif;position:relative}
.sheet{position:absolute;top:20px;width:520px;height:736px;overflow:hidden}
.sheet--front{left:48px;background:var(--paper)}
.sheet--back{left:632px;background:var(--paper-grey)}
.abs{position:absolute}
.shapes{position:absolute;inset:0;width:100%;height:100%}

/* brand */
.brand{display:flex;align-items:center;gap:8px}
.brand__dot{border-radius:50%;background:var(--teal);flex:none}
.brand__text{display:flex;flex-direction:column;line-height:1}
.brand__name{font-weight:700;color:var(--teal)}
.brand__tag{font-weight:600;color:#666;letter-spacing:.3px}

/* question list */
.questions{list-style:none;color:#fff;font-weight:700}
.questions li{display:flex;gap:8px;align-items:flex-start}
.q-mark{flex:none;border-radius:50%;background:#fff;color:var(--teal);font-weight:800;display:flex;align-items:center;justify-content:center}

/* front */
.art-question{left:300px;top:14px;width:190px;height:310px;background:linear-gradient(160deg,#2a78c4 0%,#1d5a9c 60%,#17467c 100%);border-radius:95px 95px 24px 24px}
.front-logo{left:22px;top:18px}
.front-logo .brand__dot{width:42px;height:42px}
.front-logo .brand__name{font-size:36px}
.front-logo .brand__tag{font-size:8px;margin-top:2px}
.front-questions{left:16px;top:92px;width:262px;font-size:11.5px;line-height:1.22}
.front-questions li{margin-bottom:9px}
.front-questions .q-mark{width:15px;height:15px;font-size:10px;margin-top:1px}
.front-title{left:16px;top:352px;color:#fff;line-height:1}
.front-title__main{font-weight:900;font-size:25px;letter-spacing:.5px}
.front-title__sub{font-weight:500;font-size:25px;letter-spacing:.5px;margin-top:3px}
.photo-coach{left:0;top:418px;width:262px;height:318px;background:linear-gradient(160deg,#8a7a68 0%,#7a2a30 45%,#6a1d25 100%)}

.contact{left:272px;top:400px;width:248px;display:flex;flex-direction:column;align-items:center;text-align:center}
.contact .brand__dot{width:50px;height:50px}
.contact .brand__name{font-size:52px}
.contact .brand__tag{font-size:9.5px;margin-top:2px}
.icon{width:28px;height:28px;border-radius:50%;background:var(--teal);display:flex;align-items:center;justify-content:center}
.icon svg{width:15px;height:15px}
.phone-pill{margin-top:8px;background:var(--teal);color:#fff;font-weight:600;font-size:19px;padding:5px 22px;border-radius:16px;letter-spacing:.5px}
.contact__line{font-weight:500;color:#333;margin-top:5px}
.contact__email{font-size:12px}
.contact__web{font-size:15px}
.rule{width:200px;height:1px;background:var(--teal);margin-top:10px}
.cheque-note{font-size:10.5px;color:#333;margin-top:6px}
.partner{font-weight:900;color:var(--navy);font-size:26px;letter-spacing:-.5px;margin-top:2px}

/* back */
.photo-client{left:0;top:0;width:250px;height:296px;background:linear-gradient(170deg,#d9d9d9 0%,#caa060 50%,#c8962c 100%)}
.back-logo{right:26px;top:8px}
.back-logo .brand__dot{width:32px;height:32px}
.back-logo .brand__name{font-size:30px}
.back-logo .brand__tag{font-size:7px;margin-top:1px}
.back-title{left:204px;top:58px;width:310px;color:#fff;text-align:center;line-height:1}
.back-title__main{font-weight:900;font-size:20px}
.back-title__sub{font-weight:500;font-size:15px;margin-top:3px}
.back-questions{left:16px;top:320px;width:244px;font-size:11.5px;line-height:1.25}
.back-questions li{margin-bottom:11px}
.back-questions .q-mark{width:16px;height:16px;font-size:11px;margin-top:1px}
.benefits{left:352px;top:122px;width:154px;color:var(--grey-text);font-size:8.6px;line-height:1.32;text-align:justify}
.benefit{position:relative;padding-bottom:9px;margin-bottom:9px;border-bottom:1px solid var(--teal)}
.benefit__icon{position:absolute;left:-42px;top:4px;width:30px;height:30px;border-radius:50%;background:var(--teal);display:flex;align-items:center;justify-content:center}
.benefit__icon svg{width:15px;height:15px}
.closing{text-align:center;font-size:9.5px;color:#333;padding-bottom:9px;border-bottom:1px solid var(--teal)}
.back-partner{left:330px;top:662px;width:180px;text-align:center}
.back-partner .partner{font-size:26px}
.back-partner p{font-size:10px;color:#333;margin-top:2px}
</style>
</head>
<body>

<section class="sheet sheet--front">
  <div class="art-question abs" role="img" aria-label="Illustration of a large blue question mark with a silhouette of a puzzled businessman holding a briefcase"></div>

  <svg class="shapes" viewBox="0 0 520 736" aria-hidden="true">
    <polygon points="0,70 292,52 292,340 0,350" fill="var(--teal)"/>
    <polygon points="0,345 262,338 262,412 0,418" fill="var(--ink)"/>
    <polyline points="262,412 262,500 220,520 262,540 262,736" fill="none" stroke="var(--teal)" stroke-width="2"/>
  </svg>

  <div class="brand front-logo abs">
    <span class="brand__dot"></span>
    <span class="brand__text"><span class="brand__name">Vanta</span><span class="brand__tag">professional coaching</span></span>
  </div>

  <ul class="questions front-questions abs">
    <li><span class="q-mark">?</span><span>Do I fit for the job?</span></li>
    <li><span class="q-mark">?</span><span>Am I using my talents at best in this job?</span></li>
    <li><span class="q-mark">?</span><span>I have a conflict with my manager/colleagues, what should I do?</span></li>
    <li><span class="q-mark">?</span><span>My work-life balance is a mess, how can I improve this?</span></li>
    <li><span class="q-mark">?</span><span>What job fits best with my talents? I'm getting stressed out from my job, what can I do?</span></li>
  </ul>

  <h1 class="front-title abs">
    <div class="front-title__main">PROFESSIONAL</div>
    <div class="front-title__sub">JOB COACHING</div>
  </h1>

  <div class="photo-coach abs" role="img" aria-label="Photo of the coach in a red shirt standing in front of an arched window"></div>

  <div class="contact abs">
    <div class="brand">
      <span class="brand__dot"></span>
      <span class="brand__text"><span class="brand__name">Vanta</span><span class="brand__tag">professional coaching</span></span>
    </div>
    <span class="icon" style="margin-top:12px"><svg viewBox="0 0 24 24" fill="#fff"><path d="M6.6 10.8a15.1 15.1 0 0 0 6.6 6.6l2.2-2.2a1 1 0 0 1 1-.25 11.4 11.4 0 0 0 3.6.57 1 1 0 0 1 1 1V20a1 1 0 0 1-1 1A17 17 0 0 1 3 4a1 1 0 0 1 1-1h3.5a1 1 0 0 1 1 1c0 1.25.2 2.45.57 3.57a1 1 0 0 1-.25 1z"/></svg></span>
    <div class="phone-pill">0471/389145</div>
    <span class="icon" style="margin-top:12px"><svg viewBox="0 0 24 24" fill="none" stroke="#fff" stroke-width="2"><rect x="3" y="6" width="18" height="12" rx="1"/><path d="M3 7l9 6 9-6"/></svg></span>
    <div class="contact__line contact__email">tom.vermeer@vantacoaching.example</div>
    <span class="icon" style="margin-top:10px"><svg viewBox="0 0 24 24" fill="#fff"><path d="M12 2a7 7 0 0 0-7 7c0 5 7 13 7 13s7-8 7-13a7 7 0 0 0-7-7zm0 9.5A2.5 2.5 0 1 1 12 6.5a2.5 2.5 0 0 1 0 5z"/></svg></span>
    <div class="contact__line contact__web">www.vantacoaching.example</div>
    <div class="rule"></div>
    <div class="cheque-note">Career guidance cheques of the</div>
    <div class="partner">KWOL</div>
  </div>
</section>

<section class="sheet sheet--back">
  <div class="photo-client abs" role="img" aria-label="Photo of a smiling woman in a mustard jacket holding a blue clipboard and pointing upward"></div>

  <svg class="shapes" viewBox="0 0 520 736" aria-hidden="true">
    <polygon points="250,0 520,0 520,44 278,44" fill="#ffffff"/>
    <polygon points="214,50 520,44 520,104 200,112" fill="var(--teal)"/>
    <polygon points="0,306 270,296 270,312 300,330 270,350 280,736 0,736" fill="var(--teal)"/>
    <polyline points="274,292 276,310 308,330 278,352 290,736" fill="none" stroke="var(--teal-dark)" stroke-width="1.5"/>
  </svg>

  <div class="brand back-logo abs">
    <span class="brand__dot"></span>
    <span class="brand__text"><span class="brand__name">Vanta</span><span class="brand__tag">professional coaching</span></span>
  </div>

  <h2 class="back-title abs">
    <div class="back-title__main">CAREER GUIDANCE</div>
    <div class="back-title__sub">(WITH CAREER VOUCHERS)</div>
  </h2>

  <ul class="questions back-questions abs">
    <li><span class="q-mark">?</span><span>And that's where Career Counseling comes into play.</span></li>
    <li><span class="q-mark">?</span><span>During this career counseling, we take a close look at your personal situation.</span></li>
    <li><span class="q-mark">?</span><span>Do you recognize yourself in any of the following questions?</span></li>
    <li><span class="q-mark">?</span><span>How can I get more energy from my job?</span></li>
    <li><span class="q-mark">?</span><span>How can I get a better work-life balance?</span></li>
    <li><span class="q-mark">?</span><span>What are my talents?</span></li>
    <li><span class="q-mark">?</span><span>How can I work better with my manager and/or colleagues?</span></li>
    <li><span class="q-mark">?</span><span>Do you know what you want, but do not dare to take the step?</span></li>
    <li><span class="q-mark">?</span><span>Or maybe you think you have more up your sleeve than you do today?</span></li>
  </ul>

  <div class="benefits abs">
    <div class="benefit">
      <span class="benefit__icon"><svg viewBox="0 0 24 24" fill="none" stroke="#fff" stroke-width="2"><circle cx="12" cy="12" r="8"/><path d="M12 7v5l3 2"/></svg></span>
      We easily spend 8 hours a day on our professional pursuits, our job. If we assume that we sleep about 8 hours a day, that's 50% of our active time. We actually spend more time with our colleagues than with our partner and/or children.
    </div>
    <div class="benefit">
      <span class="benefit__icon"><svg viewBox="0 0 24 24" fill="#fff"><circle cx="12" cy="5" r="2.5"/><path d="M10 9h4l1 6h-2l-1 7h-1l-1-7H8z"/></svg></span>
      In addition, if things are not going well during those 8 hours, it also impacts the other 8 waking hours. If we don't feel good about ourselves at work, our family members, friends and acquaintances feel it too.
    </div>
    <div class="benefit">
      <span class="benefit__icon"><svg viewBox="0 0 24 24" fill="none" stroke="#fff" stroke-width="2"><path d="M5 12l5 5 9-10"/></svg></span>
      So we'd better make sure that we spend those 8 hours meaningfully and, at best, get energy from it too. That we can accomplish a piece of our personal accomplishments there.
    </div>
    <div class="benefit">
      <span class="benefit__icon"><svg viewBox="0 0 24 24" fill="none" stroke="#fff" stroke-width="2"><path d="M3 18l6-6 4 4 8-8"/><path d="M15 8h6v6"/></svg></span>
      Unfortunately, not every career goes smoothly, and it is even very normal that there are ups and downs this, nowadays more than 40-year career. But we can strive to keep these downs as short as possible and the ups as long as possible.
    </div>
    <p class="closing">Then we will work on this together.</p>
  </div>

  <div class="back-partner abs">
    <div class="partner">KWOL</div>
    <p>career cheques, these can be used.</p>
  </div>
</section>

</body>
</html>
```